Bramwell Resources Ltd. - Refreshed business card challenge

A revised, refreshed business card design for my oil and gas company using my existing logo. Feel free to be as creative as you like!

Target Market(s)

bankers, lawyers

Industry/Entity Type

Oil And Gas Exploration

Contact Information for Business Card

See the "Must Haves" section

Font styles to use
Serif
Sans Serif

Colors

Designer to choose colors to be used in the design.

Requirements
Must have
• Existing business logo, name, title, email, phone number, business address
• Neil Hadley, CA, CPA
• Vice President Finance & Chief Financial Officer
• nhadley@bramwellresources-mail.com
• office: (587)555-0142
• cell: (403)555-0187
• 1400, 815 4 Street S.W.
• Calgary, AB
• T2P 4K8
Should not have
• Should not be plain and boring.

```html
<!DOCTYPE html>
<html lang="en">
<head>
<meta charset="utf-8">
<title>Bramwell Resources Ltd. – Business Card</title>
<link href="https://fonts.googleapis.com/css2?family=Titillium+Web:wght@400;600;700&display=swap" rel="stylesheet">
<style>
  :root {
    --page: #e6e6e6;
    --card: #fbfbfa;
    --green: #0f5a36;
    --brown: #55280d;
    --muted: #6b5a4e;
  }
  * { box-sizing: border-box; margin: 0; padding: 0; }
  html, body { width: 1200px; height: 909px; overflow: hidden; }
  body {
    background: var(--page);
    font-family: "Titillium Web", Arial, sans-serif;
    position: relative;
  }
  .card {
    position: absolute;
    left: 50px; top: 142px;
    width: 1100px; height: 625px;
    background: var(--card);
    box-shadow: 0 6px 24px rgba(0,0,0,0.12);
  }
  .card__band {
    position: absolute; left: 0; right: 0; bottom: 0;
    height: 19px; background: var(--green);
  }
  .contact {
    position: absolute;
    display: flex; align-items: center; gap: 14px;
    font-size: 25px; color: var(--brown); line-height: 1;
  }
  .contact svg { width: 26px; height: 26px; fill: var(--green); flex: none; }
  .contact--office { left: 50px; top: 55px; }
  .contact--cell { right: 50px; top: 55px; }
  .contact--web { left: 50px; top: 538px; }
  .contact--email { right: 50px; top: 538px; }
  .identity {
    position: absolute; left: 0; right: 0; top: 178px;
    text-align: center;
  }
  .identity__company {
    font-size: 70px; font-weight: 700; color: var(--green);
    line-height: 1; letter-spacing: -1px;
  }
  .identity__name {
    margin-top: 26px;
    font-size: 46px; font-weight: 600; color: var(--brown); line-height: 1;
  }
  .identity__credentials {
    font-size: 26px; font-weight: 400; color: var(--muted);
    margin-left: 14px;
  }
  .identity__title {
    margin-top: 10px;
    font-size: 25px; color: var(--green); line-height: 1.3;
  }
  .identity__address {
    margin-top: 6px;
    font-size: 25px; font-weight: 700; color: var(--brown); line-height: 1.3;
    letter-spacing: 0.5px;
  }
</style>
</head>
<body>
  <div class="card">
    <div class="contact contact--office">
      <svg viewBox="0 0 24 24" aria-hidden="true"><path d="M3 8c0-2 3-4 9-4s9 2 9 4v2h-5V8H8v2H3z"/><path d="M7 11h10l3 8H4z"/><circle cx="12" cy="15" r="2" fill="#fbfbfa"/></svg>
      <span>(587)555-0142</span>
    </div>
    <div class="contact contact--cell">
      <svg viewBox="0 0 24 24" aria-hidden="true"><path d="M7 1h10a2 2 0 0 1 2 2v18a2 2 0 0 1-2 2H7a2 2 0 0 1-2-2V3a2 2 0 0 1 2-2zm0 3v14h10V4z"/><circle cx="12" cy="20.5" r="1.1" fill="#fbfbfa"/></svg>
      <span>(403)555-0187</span>
    </div>

    <div class="identity">
      <div class="identity__company">Bramwell Resources</div>
      <div class="identity__name">Neil Hadley<span class="identity__credentials">CA, CPA</span></div>
      <div class="identity__title">Vice President Finance &amp; Chief Financial Officer</div>
      <div class="identity__address">1400, 815 4 Street S.W. Calgary, AB, T2P 4K8</div>
    </div>

    <div class="contact contact--web">
      <svg viewBox="0 0 24 24" aria-hidden="true"><circle cx="12" cy="12" r="10"/><g fill="none" stroke="#fbfbfa" stroke-width="1.4"><ellipse cx="12" cy="12" rx="4.5" ry="10"/><path d="M2 12h20M4 7h16M4 17h16M12 2v20"/></g></svg>
      <span>www.bramwellresources-mail.com</span>
    </div>
    <div class="contact contact--email">
      <svg viewBox="0 0 24 24" aria-hidden="true"><rect x="1" y="5" width="22" height="14"/><path d="M1.5 5.5 12 13l10.5-7.5" fill="none" stroke="#fbfbfa" stroke-width="1.6"/></svg>
      <span>nhadley@bramwellresources-mail.com</span>
    </div>

    <div class="card__band"></div>
  </div>
</body>
</html>
```